Home Design company focused on remodel and enhancement of kitchens and bathroorms

I already have a logo designed by ArtHive, I now need a design for my business cards.
The company is in the remodeling and enhancement industry for homes, focusing on kitchens and bathrooms, however, we can remodel or enhance every room in a home, an office space, etc.

The company's name is VORNETT HOME DESIGN, LLC

We'll focus on clients in the Rio Grande Valley, Texas. Primarily McAllen, Edinburg, Pharr, Mission, Brownsville and South Padre Island.

The design on the business card should transmit reliability, professionalism anda bit of upscale design.

The logo is in black and white, and would like to keep it that way.

The information that needs to be printed in the business cards is:
Company's name: Vornett Home Design
My name: Mira Lindqvist
Address, phone and email:
2715 N Parkline Rd, Ste 318
Ravensby, CO 70913
(555) 731 2958
mlindqvist@vornettstudio.com
Website: vornettstudio.com

```html
<!DOCTYPE html>
<html lang="en">
<head>
<meta charset="utf-8">
<title>Vornett Home Design – Business Card</title>
<link href="https://fonts.googleapis.com/css2?family=Montserrat:wght@400;600&display=swap" rel="stylesheet">
<style>
  :root {
    --backdrop: #c3c3c3;
    --ink: #000000;
    --paper: #ffffff;
    --rule: #bdbdbd;
  }
  * { margin: 0; padding: 0; box-sizing: border-box; }
  html, body { width: 960px; height: 1200px; overflow: hidden; }
  body {
    background: var(--backdrop);
    font-family: "Montserrat", sans-serif;
    position: relative;
  }
  .card {
    position: absolute;
    left: 83px;
    width: 795px;
    height: 455px;
    overflow: hidden;
  }
  .card--front { top: 81px; background: var(--paper); }
  .card--back { top: 648px; background: var(--ink); }

  .front-band {
    position: absolute; left: 0; top: 0;
    width: 100%; height: 218px;
    background: var(--ink);
  }
  .brand {
    position: absolute;
    left: 0; width: 100%;
    display: flex; align-items: center; justify-content: center;
    gap: 12px;
    color: var(--paper);
    font-weight: 400;
    letter-spacing: 0.22em;
    text-transform: uppercase;
    white-space: nowrap;
  }
  .brand__mark {
    width: 14px; height: 14px;
    border: 2px solid var(--paper);
  }
  .front-band .brand { top: 76px; font-size: 22px; }
  .front-band .divider {
    position: absolute; left: 294px; top: 139px;
    width: 195px; height: 1px; background: var(--paper); opacity: .8;
  }
  .holder-name {
    position: absolute; left: 0; top: 155px; width: 100%;
    text-align: center;
    color: var(--paper);
    font-weight: 600; font-size: 19px; letter-spacing: -0.01em;
  }

  .contact {
    position: absolute;
    display: flex; align-items: flex-start; gap: 10px;
    color: var(--ink); font-size: 17px; line-height: 23px;
    white-space: nowrap;
  }
  .contact__icon {
    width: 38px; height: 38px; flex: none;
    margin-top: -8px;
  }
  .contact--phone { left: 86px; top: 282px; }
  .contact--email { left: 356px; top: 280px; }
  .contact--web   { left: 86px; top: 353px; }
  .contact--addr  { left: 356px; top: 353px; }

  .card--back .brand { top: 210px; font-size: 26px; }
  .back-footer {
    position: absolute; left: 0; top: 405px; width: 100%;
    display: flex; align-items: center; gap: 10px;
  }
  .back-footer__rule { flex: 1; height: 1px; background: var(--rule); margin-top: 6px; }
  .back-footer__site { color: var(--paper); font-size: 17px; }
</style>
</head>
<body>

<section class="card card--front">
  <div class="front-band">
    <div class="brand"><span class="brand__mark"></span>Vornett Home Design</div>
    <div class="divider"></div>
    <div class="holder-name">MIRA LINDQVIST</div>
  </div>

  <div class="contact contact--phone">
    <svg class="contact__icon" viewBox="0 0 38 38" aria-hidden="true">
      <circle cx="19" cy="19" r="19" fill="#000"/>
      <path d="M13 11c1-1 2-1 3 0l2 3c.6 1 .3 1.8-.5 2.4l-1 .8c.8 2 2.3 3.6 4.3 4.5l.8-1c.6-.8 1.5-1 2.4-.5l3 2c1 .7 1 1.8 0 2.8l-1.3 1.3c-1.3 1.2-3.5 1.1-6-.4-3-1.8-5.6-4.4-7.3-7.4-1.4-2.5-1.4-4.6-.2-5.8z" fill="#fff"/>
      <path d="M21 10a7 7 0 0 1 7 7M21 13a4 4 0 0 1 4 4" stroke="#fff" stroke-width="1.6" fill="none" stroke-linecap="round"/>
    </svg>
    <span>(555) 731 2958</span>
  </div>

  <div class="contact contact--email">
    <svg class="contact__icon" viewBox="0 0 38 38" aria-hidden="true">
      <circle cx="19" cy="19" r="19" fill="#000"/>
      <rect x="10" y="13" width="18" height="12" fill="none" stroke="#fff" stroke-width="1.6"/>
      <path d="M10 13l9 7 9-7M10 25l6.5-6M28 25l-6.5-6" stroke="#fff" stroke-width="1.4" fill="none"/>
    </svg>
    <span>mlindqvist@vornettstudio.com</span>
  </div>

  <div class="contact contact--web">
    <svg class="contact__icon" viewBox="0 0 38 38" aria-hidden="true">
      <circle cx="19" cy="19" r="19" fill="#000"/>
      <g stroke="#fff" stroke-width="1.5" fill="none">
        <circle cx="19" cy="19" r="10"/>
        <ellipse cx="19" cy="19" rx="4.5" ry="10"/>
        <path d="M9 19h20M10.5 14h17M10.5 24h17M19 9v20"/>
      </g>
    </svg>
    <span>vornettstudio.com</span>
  </div>

  <div class="contact contact--addr">
    <svg class="contact__icon" viewBox="0 0 38 38" aria-hidden="true">
      <circle cx="19" cy="19" r="19" fill="#000"/>
      <path d="M19 9a7 7 0 0 0-7 7c0 5 7 13 7 13s7-8 7-13a7 7 0 0 0-7-7z" fill="#fff"/>
      <circle cx="19" cy="16" r="2.8" fill="#000"/>
    </svg>
    <span>2715 N Parkline Rd, Ste 318<br>Ravensby, CO 70913</span>
  </div>
</section>

<section class="card card--back">
  <div class="brand"><span class="brand__mark"></span>Vornett Home Design</div>
  <div class="back-footer">
    <span class="back-footer__rule"></span>
    <span class="back-footer__site">vornettstudio.com</span>
    <span class="back-footer__rule"></span>
  </div>
</section>

</body>
</html>
```